Real Estate Managemene Company Needs Business Card Design

We have a logo design and just need business cards made now for our business. Please use PDF logo # 3.

Card with Information to be attached shortly.

The card is used for a real estate management company. We will need to add four other employees and their cards.

Industry/Entity Type

Real Estate

Contact Information for Business Card

Tariq Hamdan
President
3187 Thornwick Avenue
Suite C
Glendale Heights, IL 60152
Phone 630.417.2286
Fax 630.417.2287
Cell 630.473.8062
vantorp@mailbreeze.net

Once design is approved we will have four other employees
Omar Hamdan
Operations Manager

Nadia Hamdan
Administrative Manager

Faz Hamdan
Principal

We would need to take out the cell # 630.473.8062 out for the remaining three cards.

Requirements
Must have
• Please use logo attached

```html
<!DOCTYPE html>
<html lang="en">
<head>
<meta charset="utf-8">
<title>Meridian Property Management – Business Card</title>
<link rel="stylesheet" href="https://fonts.googleapis.com/css2?family=Dosis:wght@400;500;600&family=Lato:wght@300;400&display=swap">
<style>
  :root {
    --bg: #e4e5e7;
    --paper: #ffffff;
    --blue: #0a5fb0;
    --blue-deep: #063a7e;
    --ink: #1d1d1f;
    --rule: #1f67b3;
  }
  * { margin: 0; padding: 0; box-sizing: border-box; }
  html, body { width: 1200px; height: 800px; overflow: hidden; }
  body {
    background: var(--bg);
    position: relative;
    font-family: "Dosis", "Arial Narrow", sans-serif;
    color: var(--ink);
  }
  .card {
    position: absolute;
    left: 75px; top: 100px;
    width: 1050px; height: 600px;
    background: var(--paper);
    overflow: hidden;
    box-shadow: 0 10px 30px rgba(0,0,0,0.12);
  }
  .card__band { position: absolute; inset: 0; width: 100%; height: 100%; }
  .holder {
    position: absolute;
    left: 350px; top: 110px;
  }
  .holder__title { font-size: 30px; font-weight: 400; letter-spacing: 0.5px; }
  .holder__name {
    font-family: "Lato", "Helvetica", sans-serif;
    font-weight: 300;
    font-size: 46px;
    color: var(--blue);
    line-height: 1.05;
  }
  .brand {
    position: absolute;
    right: 70px; top: 250px;
    display: flex; align-items: center; gap: 14px;
  }
  .brand__mark { width: 22px; height: 22px; background: var(--ink); }
  .brand__name {
    font-size: 30px; font-weight: 500; letter-spacing: 1px;
    text-transform: uppercase; color: var(--ink); line-height: 1;
  }
  .contact {
    position: absolute;
    right: 62px; top: 330px;
    list-style: none;
    text-align: right;
  }
  .contact__item {
    font-size: 27px; line-height: 38px;
    display: flex; justify-content: flex-end; align-items: center; gap: 10px;
  }
  .contact__icon { width: 20px; height: 20px; fill: var(--rule); }
  .divider {
    position: absolute;
    left: 330px; right: 62px; top: 490px;
    height: 2px; background: var(--rule);
  }
  .address {
    position: absolute;
    right: 62px; top: 502px;
    text-align: right;
    font-style: normal;
    font-size: 30px; line-height: 36px;
  }
</style>
</head>
<body>
  <article class="card">
    <svg class="card__band" viewBox="0 0 1050 600" role="img" aria-label="Blue band with faint building and house illustration">
      <defs>
        <linearGradient id="bandTone" x1="0" y1="0" x2="1" y2="1">
          <stop offset="0" stop-color="#0b63b8"/>
          <stop offset="1" stop-color="#052f6f"/>
        </linearGradient>
      </defs>
      <polygon points="0,0 310,0 225,360 265,600 0,600" fill="url(#bandTone)"/>
    </svg>

    <header class="holder">
      <p class="holder__title">President</p>
      <h1 class="holder__name">Tariq Hamdan</h1>
    </header>

    <div class="brand">
      <span class="brand__mark"></span>
      <span class="brand__name">Meridian Property Management</span>
    </div>

    <ul class="contact">
      <li class="contact__item">555.417.2286
        <svg class="contact__icon" viewBox="0 0 20 20" aria-hidden="true"><path d="M5 2h3l1 4-2 1.5a11 11 0 0 0 5.5 5.5L14 11l4 1v3c0 1-1 2-2 2C9 17 3 11 3 4c0-1 1-2 2-2z"/></svg>
      </li>
      <li class="contact__item">555.417.2287
        <svg class="contact__icon" viewBox="0 0 20 20" aria-hidden="true"><rect x="5" y="2" width="10" height="6" rx="1"/><rect x="2" y="8" width="16" height="10" rx="2"/></svg>
      </li>
      <li class="contact__item">555.473.8062
        <svg class="contact__icon" viewBox="0 0 20 20" aria-hidden="true"><path d="M6 1h8a1 1 0 0 1 1 1v16a1 1 0 0 1-1 1H6a1 1 0 0 1-1-1V2a1 1 0 0 1 1-1zm1 2v12h6V3z"/></svg>
      </li>
      <li class="contact__item">vantorp@mailbreeze.net
        <svg class="contact__icon" viewBox="0 0 20 20" aria-hidden="true"><path d="M2 5h16v11H2z M2 5l8 6 8-6" stroke="#fff" stroke-width="1.2"/></svg>
      </li>
    </ul>

    <div class="divider"></div>

    <address class="address">
      3187 Thornwick Avenue<br>
      Suite C, Harlow Springs, OR 97418
    </address>
  </article>
</body>
</html>
```